We need a web design for a retail food business based in Greater Western Sydney Australia called Golden Lantern Noodle Restaurant. Basically just need a simple yet easily to navigate website to browse through a menu, gallery , brief description about us, opening hours.
Menu and Gallery will be constantly updated.
Will provide own images for gallery
Updates
Menu has been uploaded and some idea on the colours I would like on the site
Some additional pictures added to see what designs you guys can come up with . Thanks again
To All Designers,
Any extra fee on top of the designs that feels need to be charged, please let me know in advance
Reason: Extending Deadline as I have yet to find a design that I would like...Thanks guys
Target Market(s)
All groups
Industry/Entity Type
Business
Requirements
Must have
- Open minded to any designs
Nice to have
- Would like slideshow behind main logo.
Preferred light coloured site yet not too playful
Should not have
- Preferably no dark colours backgrounds

```html
<!DOCTYPE html>
<html lang="en">
<head>
<meta charset="utf-8">
<title>Golden Lantern Noodle Restaurant – Homepage Colour Options</title>
<link rel="stylesheet" href="https://fonts.googleapis.com/css2?family=Open+Sans:wght@400;600;700;800&family=Ubuntu:wght@400;700&display=swap">
<style>
  :root {
    --page-bg: #ffffff;
    --bar-black: #000000;
    --footer-black: #1c1b1b;
    --nav-text: #ffffff;
    --nav-active: #e8321f;
    --brand-red: #d6301c;
    --card-red: #df3a24;
    --card-edge: #6e1a10;
    --icon-black: #0d0d0d;
    --icon-white: #ffffff;
    --label-ink: #1a1a1a;
    --desc-red: #e0321e;
    --footer-muted: #8a8a8a;
    --footer-text: #e6e6e6;
    --footer-icon: #bdbdbd;
    --band-olive: #d2d47c;
    --band-olive-deep: #c5b862;
    --band-pink: #f6ccd6;
    --band-pink-deep: #f0b6c3;
    --caption-ink: #222222;
  }
  * { box-sizing: border-box; margin: 0; padding: 0; }
  html, body {
    width: 1200px; height: 1000px; overflow: hidden;
    background: var(--page-bg);
    font-family: "Open Sans", Arial, sans-serif;
  }
  .board { position: relative; width: 1200px; height: 1000px; }

  .mockup {
    position: absolute; top: 145px; width: 585px; height: 637px;
    overflow: hidden;
  }
  .mockup--olive { left: 10px; }
  .mockup--pink { left: 607px; }

  /* top navigation */
  .topbar {
    position: absolute; left: 0; top: 0; width: 585px; height: 36px;
    background: var(--bar-black);
  }
  .topbar__brand {
    position: absolute; left: 39px; top: 10px;
    font-size: 10.5px; color: var(--nav-text); letter-spacing: 0.2px;
  }
  .topbar__nav {
    position: absolute; left: 186px; top: 13px;
    display: flex; gap: 10px; list-style: none;
    font-size: 7.5px; color: var(--nav-text); text-transform: uppercase;
  }
  .topbar__nav .is-active { color: var(--nav-active); }
  .topbar__search {
    position: absolute; left: 434px; top: 10px; width: 99px; height: 12px;
    border-radius: 6px; background: #ffffff;
    font-size: 5px; color: #777; padding: 3px 0 0 7px;
  }

  /* slider */
  .slider {
    position: absolute; left: 0; top: 36px; width: 585px; height: 241px;
  }
  .slider__photo {
    position: absolute; inset: 0;
    background:
      radial-gradient(ellipse 55% 45% at 45% 78%, #c48a62 0%, #a2503a 45%, transparent 75%),
      radial-gradient(ellipse 40% 30% at 42% 25%, #56585c 0%, transparent 70%),
      linear-gradient(160deg, #f4f1ec 0%, #e6dccd 40%, #c7a57c 75%, #b48c62 100%);
  }
  .slider__title {
    position: absolute; left: 0; width: 585px; top: 54px; text-align: center;
    font-weight: 700; font-size: 20px; color: #ffffff;
    text-shadow: 0 0 3px rgba(0,0,0,0.7);
  }
  .slider__caption {
    position: absolute; left: 0; width: 585px; top: 102px; text-align: center;
    font-size: 18.5px; line-height: 24px; color: #ffffff;
    text-shadow: 0 0 3px rgba(0,0,0,0.8);
  }
  .slider__arrow {
    position: absolute; top: 102px; width: 18px; height: 18px; border-radius: 50%;
    background: rgba(255,255,255,0.85); border: 1px solid #9a9a9a;
  }
  .slider__arrow--prev { left: 6px; }
  .slider__arrow--next { left: 558px; }
  .slider__arrow svg { display: block; }

  /* feature band */
  .features {
    position: absolute; left: 0; top: 277px; width: 585px; height: 265px;
  }
  .mockup--olive .features {
    background:
      radial-gradient(ellipse 22% 45% at 8% 40%, var(--band-olive-deep) 0%, transparent 80%),
      radial-gradient(ellipse 10% 45% at 96% 50%, var(--band-olive-deep) 0%, transparent 80%),
      var(--band-olive);
  }
  .mockup--pink .features {
    background:
      radial-gradient(ellipse 22% 45% at 8% 40%, var(--band-pink-deep) 0%, transparent 80%),
      radial-gradient(ellipse 10% 45% at 96% 50%, var(--band-pink-deep) 0%, transparent 80%),
      var(--band-pink);
  }
  .features__brand {
    position: absolute; left: 0; width: 585px; top: 30px; text-align: center;
    font-weight: 800; font-size: 44px; line-height: 60px; color: var(--brand-red);
    text-transform: uppercase; letter-spacing: 1px;
  }
  .feature {
    position: absolute; top: 117px; width: 156px; text-align: center;
  }
  .feature:nth-of-type(1) { left: 39px; }
  .feature:nth-of-type(2) { left: 209px; }
  .feature:nth-of-type(3) { left: 378px; }
  .feature__tile {
    width: 156px; height: 94px; background: var(--card-red);
    border-radius: 3px; box-shadow: 1px 2px 0 var(--card-edge), 0 0 0 1px #b52a18;
    display: flex; align-items: center; justify-content: center;
  }
  .feature__label {
    margin-top: 5px; font-size: 15px; color: var(--label-ink); line-height: 18px;
  }
  .feature__desc {
    font-size: 7.5px; color: var(--desc-red); line-height: 11px;
  }

  /* footer */
  .footer {
    position: absolute; left: 0; top: 542px; width: 585px; height: 95px;
    background: var(--footer-black); font-family: "Ubuntu", Arial, sans-serif;
  }
  .footer__item {
    position: absolute; top: 25px; width: 110px; margin-left: -55px; text-align: center;
  }
  .footer__item:nth-child(1) { left: 107px; }
  .footer__item:nth-child(2) { left: 230px; }
  .footer__item:nth-child(3) { left: 353px; }
  .footer__item:nth-child(4) { left: 477px; }
  .footer__kicker {
    font-size: 4.5px; color: var(--footer-muted); text-transform: uppercase; letter-spacing: 0.4px;
  }
  .footer__title {
    margin-top: 2px; font-size: 7.5px; font-weight: 700; color: var(--footer-text);
  }
  .footer__icon { margin-top: 6px; display: flex; justify-content: center; height: 18px; align-items: center; }
  .footer__dot { width: 12px; height: 12px; border-radius: 50%; background: var(--footer-icon); }

  .option-label {
    position: absolute; top: 825px; width: 300px; margin-left: -150px; text-align: center;
    font-family: "Open Sans", Verdana, sans-serif; font-size: 36px; color: var(--caption-ink);
  }
  .option-label--one { left: 303px; }
  .option-label--two { left: 920px; }
</style>
</head>
<body>
<main class="board">

  <section class="mockup mockup--olive" aria-label="Homepage colour option 1">
    <header class="topbar">
      <div class="topbar__brand">GOLDEN LANTERN</div>
      <ul class="topbar__nav">
        <li class="is-active">Home</li><li>Menu</li><li>Gallery</li><li>About Us</li><li>Hours</li>
      </ul>
      <div class="topbar__search">Search</div>
    </header>
    <div class="slider">
      <div class="slider__photo" role="img" aria-label="Slideshow photo of assorted sushi on a red plate with chopsticks and a soy dish"></div>
      <div class="slider__title">Welcome!</div>
      <div class="slider__caption">This is a slider that rotates pictures<br>with a text overlay.</div>
      <div class="slider__arrow slider__arrow--prev"><svg width="16" height="16" viewBox="0 0 16 16"><path d="M9.5 4.5 6 8l3.5 3.5" fill="none" stroke="#777" stroke-width="1.8"/></svg></div>
      <div class="slider__arrow slider__arrow--next"><svg width="16" height="16" viewBox="0 0 16 16"><path d="M6.5 4.5 10 8l-3.5 3.5" fill="none" stroke="#777" stroke-width="1.8"/></svg></div>
    </div>
    <div class="features" role="img" aria-label="Faded dragon illustration and calligraphy behind the restaurant name">
      <div class="features__brand">Golden Lantern</div>
      <div class="feature">
        <div class="feature__tile">
          <svg width="100" height="70" viewBox="0 0 100 70"><ellipse cx="46" cy="42" rx="36" ry="20" fill="var(--icon-black)"/><ellipse cx="46" cy="35" rx="32" ry="11" fill="var(--icon-white)"/><path d="M30 38 92 8M34 41 96 22" stroke="var(--icon-black)" stroke-width="3.5"/></svg>
        </div>
        <div class="feature__label">Menu</div>
        <div class="feature__desc">Short description here if you'd like.</div>
      </div>
      <div class="feature">
        <div class="feature__tile">
          <svg width="100" height="70" viewBox="0 0 100 70"><rect x="4" y="14" width="92" height="52" rx="3" fill="var(--icon-black)"/><rect x="30" y="4" width="40" height="14" rx="2" fill="var(--icon-black)"/><rect x="4" y="24" width="92" height="32" fill="var(--icon-white)"/><circle cx="50" cy="40" r="23" fill="var(--icon-black)"/><circle cx="50" cy="40" r="17" fill="var(--icon-white)"/><circle cx="50" cy="40" r="12" fill="var(--icon-black)"/><circle cx="46" cy="36" r="3" fill="var(--icon-white)"/></svg>
        </div>
        <div class="feature__label">Gallery</div>
        <div class="feature__desc">Short description here if you'd like.</div>
      </div>
      <div class="feature">
        <div class="feature__tile">
          <svg width="70" height="70" viewBox="0 0 70 70"><circle cx="35" cy="35" r="30" fill="var(--icon-white)" stroke="var(--icon-black)" stroke-width="3"/><circle cx="38" cy="19" r="5" fill="var(--icon-black)"/><path d="M28 30h13l-6 20h6l-1 4H25l5-20h-3z" fill="var(--icon-black)"/></svg>
        </div>
        <div class="feature__label">About Us</div>
        <div class="feature__desc">Short description here if you'd like.</div>
      </div>
    </div>
    <footer class="footer">
      <div class="footer__item"><div class="footer__kicker">Get the latest</div><div class="footer__title">Follow Us on Chirpline</div><div class="footer__icon"><span class="footer__dot"></span></div></div>
      <div class="footer__item"><div class="footer__kicker">Like us</div><div class="footer__title">We're on Friendboard</div><div class="footer__icon"><span class="footer__dot"></span></div></div>
      <div class="footer__item"><div class="footer__kicker">Keep in touch</div><div class="footer__title">Say Hello here</div><div class="footer__icon"><svg width="20" height="16" viewBox="0 0 20 16"><rect x="1" y="1" width="18" height="14" fill="none" stroke="var(--footer-icon)" stroke-width="2"/><path d="M1 2l9 7 9-7" fill="none" stroke="var(--footer-icon)" stroke-width="2"/></svg></div></div>
      <div class="footer__item"><div class="footer__kicker">Call us</div><div class="footer__title">+1 (888) 555-0142</div><div class="footer__icon"><svg width="18" height="18" viewBox="0 0 18 18"><path d="M4 1l3 4-2 2c1 2 4 5 6 6l2-2 4 3-2 3C8 17 1 10 1 3z" fill="var(--footer-icon)"/></svg></div></div>
    </footer>
  </section>

  <section class="mockup mockup--pink" aria-label="Homepage colour option 2">
    <header class="topbar">
      <div class="topbar__brand">GOLDEN LANTERN</div>
      <ul class="topbar__nav">
        <li class="is-active">Home</li><li>Menu</li><li>Gallery</li><li>About Us</li><li>Hours</li>
      </ul>
      <div class="topbar__search">Search</div>
    </header>
    <div class="slider">
      <div class="slider__photo" role="img" aria-label="Slideshow photo of assorted sushi on a red plate with chopsticks and a soy dish"></div>
      <div class="slider__title">Welcome!</div>
      <div class="slider__caption">This is a slider that rotates pictures<br>with a text overlay.</div>
      <div class="slider__arrow slider__arrow--prev"><svg width="16" height="16" viewBox="0 0 16 16"><path d="M9.5 4.5 6 8l3.5 3.5" fill="none" stroke="#777" stroke-width="1.8"/></svg></div>
      <div class="slider__arrow slider__arrow--next"><svg width="16" height="16" viewBox="0 0 16 16"><path d="M6.5 4.5 10 8l-3.5 3.5" fill="none" stroke="#777" stroke-width="1.8"/></svg></div>
    </div>
    <div class="features" role="img" aria-label="Faded dragon illustration and calligraphy behind the restaurant name">
      <div class="features__brand">Golden Lantern</div>
      <div class="feature">
        <div class="feature__tile">
          <svg width="100" height="70" viewBox="0 0 100 70"><ellipse cx="46" cy="42" rx="36" ry="20" fill="var(--icon-black)"/><ellipse cx="46" cy="35" rx="32" ry="11" fill="var(--icon-white)"/><path d="M30 38 92 8M34 41 96 22" stroke="var(--icon-black)" stroke-width="3.5"/></svg>
        </div>
        <div class="feature__label">Menu</div>
        <div class="feature__desc">Short description here if you'd like.</div>
      </div>
      <div class="feature">
        <div class="feature__tile">
          <svg width="100" height="70" viewBox="0 0 100 70"><rect x="4" y="14" width="92" height="52" rx="3" fill="var(--icon-black)"/><rect x="30" y="4" width="40" height="14" rx="2" fill="var(--icon-black)"/><rect x="4" y="24" width="92" height="32" fill="var(--icon-white)"/><circle cx="50" cy="40" r="23" fill="var(--icon-black)"/><circle cx="50" cy="40" r="17" fill="var(--icon-white)"/><circle cx="50" cy="40" r="12" fill="var(--icon-black)"/><circle cx="46" cy="36" r="3" fill="var(--icon-white)"/></svg>
        </div>
        <div class="feature__label">Gallery</div>
        <div class="feature__desc">Short description here if you'd like.</div>
      </div>
      <div class="feature">
        <div class="feature__tile">
          <svg width="70" height="70" viewBox="0 0 70 70"><circle cx="35" cy="35" r="30" fill="var(--icon-white)" stroke="var(--icon-black)" stroke-width="3"/><circle cx="38" cy="19" r="5" fill="var(--icon-black)"/><path d="M28 30h13l-6 20h6l-1 4H25l5-20h-3z" fill="var(--icon-black)"/></svg>
        </div>
        <div class="feature__label">About Us</div>
        <div class="feature__desc">Short description here if you'd like.</div>
      </div>
    </div>
    <footer class="footer">
      <div class="footer__item"><div class="footer__kicker">Get the latest</div><div class="footer__title">Follow Us on Chirpline</div><div class="footer__icon"><span class="footer__dot"></span></div></div>
      <div class="footer__item"><div class="footer__kicker">Like us</div><div class="footer__title">We're on Friendboard</div><div class="footer__icon"><span class="footer__dot"></span></div></div>
      <div class="footer__item"><div class="footer__kicker">Keep in touch</div><div class="footer__title">Say Hello here</div><div class="footer__icon"><svg width="20" height="16" viewBox="0 0 20 16"><rect x="1" y="1" width="18" height="14" fill="none" stroke="var(--footer-icon)" stroke-width="2"/><path d="M1 2l9 7 9-7" fill="none" stroke="var(--footer-icon)" stroke-width="2"/></svg></div></div>
      <div class="footer__item"><div class="footer__kicker">Call us</div><div class="footer__title">+1 (888) 555-0142</div><div class="footer__icon"><svg width="18" height="18" viewBox="0 0 18 18"><path d="M4 1l3 4-2 2c1 2 4 5 6 6l2-2 4 3-2 3C8 17 1 10 1 3z" fill="var(--footer-icon)"/></svg></div></div>
    </footer>
  </section>

  <div class="option-label option-label--one">Color 1</div>
  <div class="option-label option-label--two">Color 2</div>

</main>
</body>
</html>
```